Versiloom Needs Several Greeting Card Shell Designs and Designs for 8.5" x 11" Prints

Versiloom Ltd. Co. is a publisher of social expression in the form of acrostic poems on greeting cards, prints, mugs, T-shirts, and a host of other products. "Acrostic" simply means spelling out something going down the page. ALL of our products are done in the acrostic style.
We have the following needs:
1) Three feminine greeting card shells designs. One design should allow for up to six lines of text to be added later. The other two designs should allow for up to 10 lines of text to be added later. These designs will be mostly aimed at tweens to young adults.
2)Three masculine greeting card shells designs. One design should allow for up to six lines of text to be added later. The other two designs should allow for up to 10 lines of text to be added later. These designs will be mostly aimed at tweens to young adults.
3) Three feminine design shells for 8.5" x 11" prints, with room for text to be added later. These designs will be aimed at a more mature audience (young adults and up).
4) Three neutral design shells for 8.5" x 11" prints, with room for text to be added later. Three feminine design shells for 8.5" x 11" prints, with room for text to be added later. These designs will be aimed at a more mature audience (young adults and up).
For samples of previous designs, please go to http://www.versiloom.example. We are looking for more current, trendy designs.

```html
<!DOCTYPE html>
<html lang="en">
<head>
<meta charset="utf-8">
<title>Versiloom Print Shell – Billiards</title>
<link rel="stylesheet" href="https://fonts.googleapis.com/css2?family=Alegreya:ital,wght@1,400&family=Nunito:ital,wght@1,900&display=swap">
<style>
  :root {
    --paper: #ffffff;
    --felt-light: #34a55a;
    --felt-mid: #2a944e;
    --felt-dark: #1f7f42;
    --frame-shade: rgba(0, 40, 15, 0.28);
    --panel: rgba(18, 110, 70, 0.78);
    --panel-line: rgba(255, 255, 255, 0.85);
    --title-fill: #1a7a48;
    --text: #ffffff;
  }
  html, body {
    margin: 0;
    padding: 0;
    width: 933px;
    height: 1200px;
    overflow: hidden;
    background: var(--paper);
  }
  .print {
    position: relative;
    width: 933px;
    height: 1200px;
    background: var(--paper);
  }
  .table-felt {
    position: absolute;
    left: 12px;
    top: 12px;
    width: 909px;
    height: 1176px;
    background:
      radial-gradient(ellipse at 50% 45%, var(--felt-light) 0%, var(--felt-mid) 60%, var(--felt-dark) 100%);
  }
  .felt-frame {
    position: absolute;
    left: 39px;
    top: 39px;
    width: 855px;
    height: 1121px;
    box-sizing: border-box;
    border: 3px solid var(--frame-shade);
    box-shadow: inset 0 0 0 1px rgba(255, 255, 255, 0.08);
  }
  .text-panel {
    position: absolute;
    left: 83px;
    top: 104px;
    width: 767px;
    height: 993px;
    box-sizing: border-box;
    background: var(--panel);
    border: 2px solid var(--panel-line);
  }
  .title {
    position: absolute;
    left: 0;
    right: 0;
    top: 108px;
    margin: 0;
    text-align: center;
    font-family: "Nunito", "Verdana", sans-serif;
    font-style: italic;
    font-weight: 900;
    font-size: 98px;
    line-height: 1;
    letter-spacing: 1px;
    color: var(--title-fill);
    -webkit-text-stroke: 12px var(--text);
    paint-order: stroke fill;
  }
  .verse {
    position: absolute;
    left: 0;
    right: 0;
    top: 272px;
    margin: 0;
    text-align: center;
    font-family: "Alegreya", "Georgia", serif;
    font-style: italic;
    font-weight: 400;
    font-size: 41px;
    line-height: 62.5px;
    color: var(--text);
  }
</style>
</head>
<body>
  <main class="print">
    <div class="table-felt" role="img" aria-label="Green billiard table felt with scattered numbered pool balls and the tip of a cue"></div>
    <div class="felt-frame"></div>
    <section class="text-panel">
      <h1 class="title">Lorem</h1>
      <p class="verse">
        Dolor sit amet, consectetur<br>
        adipisicing elit, sed do eiusmod<br>
        tempor incididunt ut labore et<br>
        dolore magna aliqua. Utt enim<br>
        ad minim veniam, quis nostrud<br>
        exercitation ullamco laboris nisi<br>
        ut aliquip ex ea commodo<br>
        consequat. Duis aute irure dolor<br>
        in reprehenderit in voluptate<br>
        velit esse cillum dolore eu nulla
      </p>
    </section>
  </main>
</body>
</html>
```